WP website design (N Kentucky)

We need a wordpress design that will incorporate a professional color scheme with company logo in a clean layout. The design needs to consider that this will be developed on a responsive theme. Colors are undetermined - can use a dark red - logo is black so creative use of colors will be important. Client wants a 'modern' look.

Industry/Entity Type

It Company

Font styles to use
Serif
Sans Serif

Requirements
Must have
• Must Have:
- Navigation: 1) Home 2) Auctions 3) Auction Marketing 4) Buying at Auction 5) About Us 6) Contact Us

Site will have a slideshow element and the following widgets: 1) Featured Auctions 2) Testimonials blog widget 3) 'Auction Alerts' email sign up 4) Fv Chirpo Lumio+ icons. Colors can be the valley38 gold/black from http://www.brambleoakdwellings.example/

In the footer, there will be smaller company logo, the affiliations logo, and contact info below:
Silver Pine Bidding, LLC / Owen Pritchley
email: owenprit@mailvex.example; owen.pritchley@v38.example
phone: (555) 274-6183 mobile phone: (555)418-7302
Domain: http://www.silverpinebidding.example/
Nice to have
• - - Site will have drop-down menus - please indicate the styling, for instance the dropdown menus 1) Upcoming Auctions 2) Past Auctions under the 'Auctions' link

```html
<!DOCTYPE html>
<html lang="en">
<head>
<meta charset="utf-8">
<title>Silver Pine Bidding, LLC</title>
<link href="https://fonts.googleapis.com/css2?family=Questrial&family=Arimo:wght@400;700&family=Open+Sans:wght@400;600&display=swap" rel="stylesheet">
<style>
:root{
  --red:#b80d12;
  --red-bright:#e0101a;
  --dark:#2b2b2b;
  --darker:#1e1e1e;
  --black:#000;
  --panel:#3a3a3a;
  --page:#dcdcdc;
  --text:#333;
  --white:#fff;
}
*{box-sizing:border-box;margin:0;padding:0}
html,body{width:711px;height:1200px;overflow:hidden}
body{position:relative;background:var(--page);font-family:"Arimo",Arial,sans-serif;color:var(--text)}
.abs{position:absolute}
/* header + hero */
.hero{left:0;top:0;width:711px;height:382px;background:linear-gradient(180deg,#5f7284 0%,#8ea3b4 35%,#6d7f8c 70%,#3b4450 100%)}
.site-header{left:0;top:0;width:711px;height:55px;background:rgba(30,34,42,.85);border-bottom:1px solid var(--red)}
.brand{left:84px;top:0;width:142px;height:55px;background:#ececec;display:flex;align-items:center;gap:6px;padding:0 8px}
.brand .mark{width:14px;height:14px;background:#222;flex:none}
.brand span{font-family:"Arimo",sans-serif;font-weight:700;font-size:11px;line-height:1.15;color:#222}
.nav{left:256px;top:0;height:55px;display:flex;font-family:"Questrial",sans-serif;font-size:7.5px;color:var(--white)}
.nav a{display:flex;align-items:center;height:55px;padding:0 11px;color:var(--white);text-decoration:none;letter-spacing:.2px}
.nav a.active{background:var(--red);padding:0 9px}
.search{left:532px;top:3px;width:94px;height:12px;background:#e6e6e6;border-radius:2px;font-size:7px;color:#999;padding:2px 4px}
.slide-prev{left:86px;top:200px;width:36px;height:36px;border-radius:50%;background:rgba(60,60,60,.7)}
.caption{left:280px;top:280px;width:431px;height:51px;background:rgba(20,24,30,.7);font-family:"Questrial",sans-serif;color:var(--white);padding:6px 0 0 35px}
.caption .t1{font-size:13px;letter-spacing:.3px}
.caption .t2{font-size:10.5px;margin-top:6px}
.caption .t2 em{font-style:normal;color:var(--red-bright)}
/* categories */
.categories{left:84px;top:356px;width:544px;height:59px;background:var(--panel);box-shadow:0 6px 8px rgba(0,0,0,.3);display:flex;gap:26px;padding:15px 16px}
.cat{width:156px;height:33px;background:#1f1f1f;display:flex;align-items:center;color:var(--white)}
.cat .ico{width:40px;height:33px;background:var(--red);display:flex;align-items:center;justify-content:center;margin-right:8px}
.cat .lbl{font-family:"Open Sans",sans-serif;font-size:10.5px;line-height:1.25}
.cat .lbl.big{font-size:13px}
/* welcome */
.welcome{left:84px;top:432px;width:360px}
h2{font-family:"Arimo",sans-serif;font-weight:400;font-size:12.5px;color:#111}
h2 em{font-style:normal;color:var(--red-bright)}
.welcome p{font-size:7px;line-height:11.5px;margin-top:9px;color:#333}
.more{font-size:8px;color:var(--red-bright);text-transform:uppercase;display:block}
.alerts{left:456px;top:432px;width:140px}
.alerts h2{font-size:10.5px}
.alerts p{font-size:7px;line-height:11.5px;margin-top:9px}
.alerts .field{width:124px;height:17px;background:var(--white);margin-top:6px;font-size:7px;color:#777;padding:4px 5px}
.alerts .btn{width:57px;height:16px;background:var(--red);color:var(--white);font-size:7px;text-align:center;line-height:16px;margin-top:6px}
/* black band */
.band{left:0;top:580px;width:711px;height:180px;background:var(--black)}
.card{top:620px;width:171px;height:125px;background:var(--panel);text-align:center;color:var(--white)}
.card .badge{position:absolute;left:67px;top:-23px;width:41px;height:39px;background:var(--red);display:flex;align-items:center;justify-content:center}
.card h3{font-family:"Open Sans",sans-serif;font-weight:400;font-size:12px;margin-top:26px}
.card h3 em{font-style:normal;color:var(--red)}
.card p{font-size:6.2px;line-height:11px;text-align:left;padding:0 8px;margin-top:6px;height:44px;overflow:hidden}
.card .btn{display:inline-block;background:var(--white);color:var(--red);font-size:6.5px;padding:4px 7px;margin-top:8px}
/* news + testimonials */
.news{left:84px;top:777px;width:264px}
.news h2,.testi h2{font-size:12px;padding-bottom:6px;border-bottom:1px solid #bbb}
.item{display:flex;margin-top:13px;position:relative}
.date{width:36px;height:30px;flex:none;border:1px solid #999;text-align:center;background:#fff}
.date .m{background:var(--red);color:#fff;font-weight:700;font-size:10px;line-height:13px}
.date .d{font-weight:700;font-size:10px;line-height:15px;color:#111}
.item .body{margin-left:8px}
.item h4{font-weight:400;font-size:7px;color:var(--red);padding-bottom:4px;border-bottom:1px dotted #aaa}
.item p{font-size:6.2px;line-height:10px;margin-top:4px}
.divider{left:354px;top:793px;width:2px;height:136px;background:#bbb}
.testi{left:362px;top:777px;width:264px}
.person{position:absolute;top:28px;width:120px}
.person .av{width:36px;height:36px;border-radius:50%;background:#fff;border:3px solid #c4c4c4}
.person .nm{position:absolute;left:44px;top:6px;font-size:6.5px;color:var(--red)}
.person .sub{position:absolute;left:44px;top:19px;font-size:6.5px;color:#111}
.person p{font-size:6.2px;line-height:10px;margin-top:5px}
/* featured strip */
.rule{left:0;top:960px;width:711px;height:1px;background:#aaa}
.tab{left:283px;top:960px;width:146px;height:21px;background:var(--red);color:#fff;text-align:center;font-size:12px;line-height:21px;border-radius:0 0 10px 10px}
.thumb{top:989px;width:153px;height:71px;border:3px solid #ccc;box-shadow:0 4px 5px rgba(0,0,0,.25)}
.thumb.active{border-color:var(--red-bright)}
/* footer */
.footer{left:0;top:1069px;width:711px;height:111px;background:var(--dark);border-top:2px solid var(--red);color:var(--white)}
.footer h5{font-family:"Open Sans",sans-serif;font-weight:400;font-size:10px}
.links{left:84px;top:15px}
.links ul{list-style:none;margin-top:8px}
.links li{font-size:6.5px;line-height:13.4px}
.links li::before{content:"> ";}
.contact{left:187px;top:15px}
.contact .row{display:flex;align-items:flex-start;gap:8px;font-size:6.8px;margin-top:9px}
.contact .row b{font-weight:700;line-height:9px}
.flogo{left:513px;top:11px;width:108px;height:41px;background:#555;display:flex;align-items:center;gap:5px;padding:0 7px}
.flogo .mark{width:10px;height:10px;background:#222;flex:none}
.flogo span{font-weight:700;font-size:8px;line-height:1.15;color:#1e1e1e}
.aff{top:68px;height:18px;background:#888}
.bottom{left:0;top:1180px;width:711px;height:20px;background:var(--black)}
</style>
</head>
<body>

<div class="abs hero" role="img" aria-label="Slideshow photo of modern glass office towers at dusk"></div>
<header class="abs site-header"></header>
<div class="abs brand"><div class="mark"></div><span>Silver Pine<br>Bidding, LLC</span></div>
<nav class="abs nav">
  <a class="active">HOME</a><a>AUCTIONS</a><a>AUCTION MARKETING</a><a>BUYING AT AUCTION</a><a>ABOUT US</a><a>CONTACT US</a>
</nav>
<div class="abs search">Search</div>
<div class="abs slide-prev"><svg width="36" height="36"><path d="M20 11l-7 7 7 7" stroke="#fff" stroke-width="3" fill="none"/></svg></div>
<div class="abs caption">
  <div class="t1">SUPERBLY LOCATED, INVITINGLY READY TO ENJOY</div>
  <div class="t2"><em>FEATURE AUCTION:</em> 42 HARLOW CRESCENT, BRENTON WA 6120</div>
</div>

<div class="abs categories">
  <div class="cat"><div class="ico"><svg width="22" height="20" fill="#fff"><rect x="2" y="7" width="6" height="13"/><rect x="9" y="2" width="6" height="18"/><rect x="16" y="9" width="5" height="11"/></svg></div><span class="lbl big">High Rises</span></div>
  <div class="cat"><div class="ico"><svg width="22" height="20" fill="#fff"><path d="M11 1l10 5H1z"/><rect x="3" y="8" width="2.5" height="8"/><rect x="8" y="8" width="2.5" height="8"/><rect x="12" y="8" width="2.5" height="8"/><rect x="17" y="8" width="2.5" height="8"/><rect x="1" y="17" width="20" height="2"/></svg></div><span class="lbl">Government Office<br>Buildings</span></div>
  <div class="cat"><div class="ico"><svg width="22" height="20" fill="none" stroke="#fff" stroke-width="1.5"><path d="M2 8l9-6 9 6v11H2z"/><path d="M6 10h3v3H6zM13 10h3v3h-3zM6 15h3v3H6zM13 15h3v3h-3z"/></svg></div><span class="lbl">Apartment<br>Communities</span></div>
</div>

<section class="abs welcome">
  <h2>Welcome to <em>Silver Pine Bidding, LLC</em></h2>
  <p>Lorem ipsum dolor sit amet, consectetur adipiscing elit. Proin pulvinar eros in imperdiet porttitor. Praesent velit justo, placerat ut ornare aliquet, venenatis vel justo. Nulla porttitor enim vitae nibh scelerisque, nec laoreet libero posuere. Integer ut neque ut purus dictum auctor. Cras tincidunt odio a pharetra iaculis. Nam in arcu eu tortor consequat tempor. Vivamus eu convallis risus.</p>
  <p>Mauris pulvinar, eros ac elementum tempus,</p>
  <span class="more" style="margin-top:14px">Read more</span>
</section>
<aside class="abs alerts">
  <h2>Auction <em>Alerts</em></h2>
  <p>Lorem Lorem aLorem is sit elitsit amet</p>
  <div class="field">Email address</div>
  <div class="btn">Subscribes</div>
</aside>

<div class="abs band"></div>
<div class="abs card" style="left:89px">
  <div class="badge"><svg width="22" height="22" fill="#fff"><rect x="3" y="6" width="7" height="15"/><rect x="11" y="2" width="8" height="19"/></svg></div>
  <h3>Featured <em>Auctions</em></h3>
  <p>Lorem ipsum dolor sit amet, consectetur adipiscing elit. Proin pulvinar eros in imperdiet porttitor. Praesent velit justo, placerat ut ornare aliquet, venenatis vel justo. Nulla porttitor enim vitae nibh scelerisque, nec laoreet libero</p>
  <span class="btn">READ MORE</span>
</div>
<div class="abs card" style="left:273px">
  <div class="badge"><svg width="24" height="24" fill="none" stroke="#fff" stroke-width="1.5"><rect x="2" y="2" width="9" height="9"/><circle cx="16" cy="16" r="6"/><path d="M16 13v6M14 14h3M14 18h3M15 4h5v4M9 20H4v-4"/></svg></div>
  <h3>Client <em>Testimonials</em></h3>
  <p>Lorem ipsum dolor sit amet, consectetur adipiscing elit. Proin pulvinar eros in imperdiet porttitor. Praesent velit justo, placerat ut ornare aliquet, venenatis vel justo. Nulla porttitor enim vitae nibh scelerisque, nec laoreet libero</p>
  <span class="btn">READ MORE</span>
</div>
<div class="abs card" style="left:457px">
  <div class="badge"><svg width="24" height="24" fill="#fff"><path d="M12 2l9 8h-3v6H6v-6H3z"/><path d="M2 20q6-4 10 0t10-2v3H2z"/></svg></div>
  <h3>Auction <em>Alerts</em></h3>
  <p>Lorem ipsum dolor sit amet, consectetur adipiscing elit. Proin pulvinar eros in imperdiet porttitor. Praesent velit justo, placerat ut ornare aliquet, venenatis vel justo. Nulla porttitor enim vitae nibh scelerisque, nec laoreet libero</p>
  <span class="btn">READ MORE</span>
</div>

<section class="abs news">
  <h2>Latest <em>News</em></h2>
  <div class="item"><div class="date"><div class="m">JAN</div><div class="d">18</div></div>
    <div class="body"><h4>Ut wisi enim ad min ve nostrud exerci ta ull amcorper</h4><p>Lorem ipsum dolor sit amet, consectetur adipiscing elit. Proin pulvinar eros in imperdiet porttitor. Praesent velit justo, placerat ut ornare aliquet, venenatis vel justo. Nulla porttitor enim vitae</p></div></div>
  <div class="item"><div class="date"><div class="m">JAN</div><div class="d">18</div></div>
    <div class="body"><h4>Ut wisi enim ad min ve nostrud exerci ta ull amcorper</h4><p>Lorem ipsum dolor sit amet, consectetur adipiscing elit. Proin pulvinar eros in imperdiet porttitor. Praesent velit justo, placerat ut ornare aliquet, venenatis vel justo. Nulla porttitor enim vitae</p></div></div>
  <span class="more" style="font-size:6.5px;margin:2px 0 0 5px;font-weight:700">Read more</span>
</section>
<div class="abs divider"></div>
<section class="abs testi">
  <h2>Clients <em>Testimonials</em></h2>
  <div class="person" style="left:0"><div class="av"></div><div class="nm">Lorem lipsum</div><div class="sub">Mr Clients Name</div>
    <p>&#8220; Lorem ipsum dolor sit amet, consectetur adipiscing elit. Proin pulvinar eros in imperdiet porttitoscelerisque, nec laoreet libero posuere. Integer ut neque ut &#8221;</p></div>
  <div class="person" style="left:139px"><div class="av"></div><div class="nm">Lorem lipsum</div><div class="sub">Mr Clients Name</div>
    <p>&#8220; Lorem ipsum dolor sit amet, consectetur adipiscing elit. Proin pulvinar eros in imperdiet porttitoscelerisque, nec laoreet libero posuere. Integer ut neque . &#8221;</p></div>
  <span class="more" style="position:absolute;top:146px;left:6px;font-size:6.5px;font-weight:700">Read more</span>
</section>

<div class="abs rule"></div>
<div class="abs tab">Featured Auctions</div>
<svg class="abs" style="left:82px;top:1016px" width="14" height="16"><path d="M10 2L3 8l7 6z" fill="#777"/></svg>
<div class="abs thumb active" style="left:100px;background:linear-gradient(160deg,#c9d3dc,#7d8c99 60%,#3a4148)" role="img" aria-label="Featured auction photo: glass office building"></div>
<svg class="abs" style="left:262px;top:1040px" width="12" height="14"><path d="M3 2l6 5-6 5" stroke="#777" stroke-width="2" fill="none"/></svg>
<div class="abs thumb" style="left:281px;background:linear-gradient(180deg,#a9c3d8,#5c7084 60%,#2f3944)" role="img" aria-label="Featured auction photo: office towers by day"></div>
<div class="abs thumb" style="left:460px;background:linear-gradient(180deg,#3d5c86,#2a3e5e 60%,#1e2633)" role="img" aria-label="Featured auction photo: city towers at dusk"></div>
<svg class="abs" style="left:616px;top:1016px" width="14" height="16"><path d="M4 2l7 6-7 6z" fill="#777"/></svg>

<footer class="abs footer">
  <div class="abs links"><h5>Quick Links</h5>
    <ul><li>Home</li><li>Company</li><li>Development</li><li>Staff</li><li>Contact</li></ul></div>
  <div class="abs contact"><h5>Contact Information</h5>
    <div class="row"><svg width="8" height="10"><path d="M4 0a3.5 3.5 0 0 1 3.5 3.5C7.5 6 4 10 4 10S.5 6 .5 3.5A3.5 3.5 0 0 1 4 0z" fill="var(--red-bright)"/><circle cx="4" cy="3.5" r="1.3" fill="#2b2b2b"/></svg><span>Silver Pine Bidding, LLC</span></div>
    <div class="row"><svg width="9" height="7"><rect width="9" height="7" fill="var(--red-bright)"/><path d="M0 0l4.5 4L9 0" stroke="#2b2b2b" fill="none"/></svg><b>owenprit@mailvex.example<br>owen.pritchley@v38.example</b></div>
    <div class="row"><svg width="8" height="9"><path d="M1 1l2-1 1.5 2.5-1 1q1 2 2.5 2.5l1-1L9 7l-1 2Q2 8 1 1z" fill="var(--red-bright)"/></svg><b>(555) 274-6183<br>(555) 418-7302</b></div>
  </div>
  <div class="abs flogo"><div class="mark"></div><span>Silver Pine<br>Bidding, LLC</span></div>
  <div class="abs aff" style="left:513px;width:20px"></div>
  <div class="abs aff" style="left:540px;width:34px;border-radius:9px"></div>
  <div class="abs aff" style="left:584px;width:38px;border-radius:50%"></div>
</footer>
<div class="abs bottom"></div>

</body>
</html>
```